New Design required for Disposable Gloves Pack

We need a new design for our range of disposable Gloves.
The brand name is "Marlow" I will attach the existing logo.

The needs to be 3 variations of the design (maybe different colours) that we can use for the different kinds of gloves: Latex Gloves, Clear Vinyl Gloves & Blue Vinyl Gloves.
Pack size is: 220x65x120mm.

Attached is a template to use showing all sides of the pack as flat. It is preferable that you supply an image of the complete folded pack as well with your design. Also attached is a PDF of our old pack design. Please use all the text on this old design for the new one.

The packs need to be easily differentiated from each other.

Target Market(s)

New Zealand Businesses, food processors & manufacturers. Medical & health care professionals

Font styles to use
Sans Serif

Requirements
Must have
• 3 variations of the same pack design to differentiate between the 3 types of gloves we offer: Latex Gloves, Clear Vinyl & Blue Vinyl Gloves.

```html
<!DOCTYPE html>
<html lang="en">
<head>
<meta charset="utf-8">
<title>Marlow Latex Gloves – Carton Net</title>
<link rel="stylesheet" href="https://fonts.googleapis.com/css2?family=Arimo:wght@400;700&family=Roboto:ital,wght@1,900&display=swap">
<style>
  :root {
    --board: #dfe24a;
    --board-light: #eef0a6;
    --glow: #ffffff;
    --brand-green: #1a9c3a;
    --olive: #6b9a2c;
    --label-yellow: #e8ec3c;
    --hand-white: #fbfcf0;
    --rule: #c9cc6a;
  }
  html, body {
    margin: 0;
    padding: 0;
    width: 1200px;
    height: 1200px;
    overflow: hidden;
    background: #ffffff;
  }
  .carton-net {
    position: absolute;
    left: 25px;
    top: 360px;
    width: 1150px;
    height: 480px;
  }
  .board { fill: var(--board); }
  .board-light { fill: var(--board-light); }
  .title-latex, .title-gloves, .size-label {
    font-family: "Roboto", "Arial Black", sans-serif;
    font-style: italic;
    font-weight: 900;
  }
  .title-latex { fill: var(--brand-green); }
  .title-gloves { fill: var(--olive); }
  .size-label { fill: var(--brand-green); }
  .label-band { fill: var(--label-yellow); }
  .brand-name {
    font-family: "Arimo", Arial, sans-serif;
    font-weight: 400;
    fill: var(--brand-green);
    letter-spacing: 2px;
  }
  .feature-list {
    font-family: "Arimo", Arial, sans-serif;
    font-size: 9.5px;
    fill: var(--brand-green);
  }
  .feature-bullet { fill: var(--brand-green); opacity: 0.7; }
  .small-print {
    font-family: "Arimo", Arial, sans-serif;
    font-weight: 700;
    font-size: 6px;
    fill: var(--brand-green);
  }
  .reorder-box { fill: none; stroke: var(--rule); stroke-width: 0.8; }
  .reorder-text {
    font-family: "Arimo", Arial, sans-serif;
    font-size: 5.5px;
    fill: var(--olive);
  }
  .hand-art { fill: var(--hand-white); }
  .dispenser-cutout { fill: none; stroke: #e2e4b0; stroke-width: 1.2; }
</style>
</head>
<body>
<svg class="carton-net" viewBox="55 895 1390 580" xmlns="http://www.w3.org/2000/svg">
  <defs>
    <radialGradient id="title-glow" cx="50%" cy="50%" r="50%">
      <stop offset="0%" stop-color="#ffffff"/>
      <stop offset="60%" stop-color="#fbfce6"/>
      <stop offset="100%" stop-color="#dfe24a" stop-opacity="0"/>
    </radialGradient>
    <linearGradient id="lid-wash" x1="0" y1="0" x2="1" y2="1">
      <stop offset="0%" stop-color="#f2f4c2"/>
      <stop offset="100%" stop-color="#e6e87a"/>
    </linearGradient>
    <clipPath id="lid-clip"><rect x="55" y="897" width="458" height="283"/></clipPath>

    <g id="main-face-art">
      <ellipse cx="195" cy="1235" rx="150" ry="68" fill="url(#title-glow)"/>
      <polygon class="label-band" points="124,1199 285,1199 280,1223 119,1223"/>
      <text class="title-latex" x="162" y="1221" font-size="25">LATEX</text>
      <text class="title-gloves" x="114" y="1256" font-size="35">GLOVES</text>
      <polygon class="label-band" points="88,1259 146,1259 142,1276 84,1276"/>
      <text class="size-label" x="88" y="1273" font-size="15">Large</text>
      <rect class="hand-art" x="300" y="1220" width="68" height="98" rx="14" role="img" aria-label="Illustration of an open white glove"/>
      <circle cx="397" cy="1225" r="4" fill="var(--brand-green)"/>
      <text class="brand-name" x="405" y="1236" font-size="17">MARLOW</text>
      <g class="feature-list">
        <rect class="feature-bullet" x="388" y="1255" width="5" height="5"/>
        <text x="400" y="1262">Ambidexterous</text>
        <rect class="feature-bullet" x="388" y="1269" width="5" height="5"/>
        <text x="400" y="1276">Single use</text>
        <rect class="feature-bullet" x="388" y="1283" width="5" height="5"/>
        <text x="400" y="1290">Lightly powered</text>
      </g>
    </g>

    <g id="end-face-art">
      <ellipse cx="620" cy="1222" rx="95" ry="52" fill="url(#title-glow)"/>
      <polygon class="label-band" points="594,1196 688,1196 685,1212 591,1212"/>
      <text class="title-latex" x="602" y="1211" font-size="16">LATEX</text>
      <text class="title-gloves" x="570" y="1235" font-size="23">GLOVES</text>
      <polygon class="label-band" points="550,1238 588,1238 585,1249 547,1249"/>
      <text class="size-label" x="550" y="1248" font-size="10">Large</text>
      <rect class="reorder-box" x="688" y="1253" width="54" height="22"/>
      <text class="reorder-text" x="692" y="1261">Reorder Code</text>
      <text class="small-print" x="741" y="1293" text-anchor="end">0800 555 019</text>
      <text class="small-print" x="741" y="1302" text-anchor="end">www.glovecarton.co.nz</text>
    </g>
  </defs>

  <!-- Lid panel (printed upside down) -->
  <rect x="55" y="897" width="458" height="283" fill="url(#lid-wash)"/>
  <g clip-path="url(#lid-clip)">
    <circle cx="520" cy="1160" r="270" fill="#f6f7d6" opacity="0.55"/>
  </g>
  <g class="lid-artwork" transform="rotate(180 284 1038)">
    <ellipse cx="175" cy="962" rx="120" ry="52" fill="url(#title-glow)"/>
    <polygon class="label-band" points="122,943 250,943 246,963 118,963"/>
    <text class="title-latex" x="150" y="961" font-size="20">LATEX</text>
    <text class="title-gloves" x="108" y="988" font-size="28">GLOVES</text>
    <polygon class="label-band" points="86,991 134,991 131,1005 83,1005"/>
    <text class="size-label" x="86" y="1003" font-size="12">Large</text>
    <rect class="dispenser-cutout" x="163" y="1012" width="237" height="57" rx="14"/>
    <circle cx="375" cy="941" r="4" fill="var(--brand-green)"/>
    <text class="brand-name" x="383" y="952" font-size="15">MARLOW</text>
    <g class="feature-list" style="font-size:8px">
      <rect class="feature-bullet" x="393" y="1073" width="4" height="4"/>
      <text x="402" y="1079">Ambidexterous</text>
      <rect class="feature-bullet" x="393" y="1087" width="4" height="4"/>
      <text x="402" y="1093">Single use</text>
      <rect class="feature-bullet" x="393" y="1101" width="4" height="4"/>
      <text x="402" y="1107">Lightly powered</text>
    </g>
  </g>
  <rect class="hand-art" x="188" y="930" width="86" height="132" rx="16" role="img" aria-label="Illustration of a glove emerging from the dispenser"/>
  <rect x="172" y="920" width="88" height="14" fill="#fbe9c8"/>

  <!-- End flaps -->
  <polygon class="board" points="524,1052 740,1052 740,1120 752,1175 513,1175 524,1120"/>
  <polygon class="board" points="1205,1052 1428,1052 1428,1120 1440,1175 1197,1175 1205,1120"/>

  <!-- Main face row -->
  <rect class="board" x="55" y="1180" width="458" height="138"/>
  <rect class="board" x="513" y="1175" width="239" height="143"/>
  <rect class="board" x="752" y="1175" width="445" height="143"/>
  <rect class="board" x="1197" y="1175" width="248" height="143"/>
  <use href="#main-face-art"/>
  <use href="#main-face-art" x="690"/>
  <use href="#end-face-art"/>
  <use href="#end-face-art" x="690"/>

  <!-- Base flaps -->
  <polygon class="board" points="55,1318 513,1318 513,1475 398,1475 398,1430 172,1430 172,1475 55,1475"/>
  <polygon class="board" points="513,1318 752,1318 752,1475 645,1475 645,1430 513,1335"/>
  <polygon class="board" points="752,1318 1197,1318 1197,1335 1085,1430 1085,1475 862,1475 862,1430 752,1335"/>
  <polygon class="board" points="1197,1318 1445,1318 1445,1330 1310,1430 1310,1475 1197,1475"/>
</svg>
</body>
</html>
```